Belford & Company

We are a boutique commercial real estate firm. For our Business card design - sleek, modern, yet high-end/classy. Please see our website: belfordandcompany.example for details.

We currently need 2 business card names and the ability to add/change the business card information -
Name, Title, Address, Office #, Mobile #, Fax, Email and company website.

Industry/Entity Type

Real Estate

Contact Information for Business Card

Business card design - sleek, modern, yet high-end/classy. Please see our website: belfordandcompany.example for details.

Also, we'd like to have our slogan "Diligence Makes The Difference." somewhere in there. We'd like to make some part of it raised or a different texture if possible.
Color #'s:
blue 19 36 128
light gray 222 222 221
dark gray 107 120 128

Also, we'd like to have our slogan "Diligence Makes The Difference." somewhere in there. We'd like to make some part of it raised or a different texture if possible - grey on one side and blue on the other - rounded edges preferred. Maybe either metal/silver/grey raised logo on the back. Thank you!!

Requirements
Must have
• Sleek, modern, clean and classy design

```html
<!DOCTYPE html>
<html lang="en">
<head>
<meta charset="utf-8">
<title>Belford &amp; Company – Business Cards</title>
<link rel="stylesheet" href="https://fonts.googleapis.com/css2?family=Ubuntu:wght@400;500;700&display=swap">
<style>
  :root {
    --brand-blue: #2e4599;
    --brand-blue-deep: #132480;
    --light-gray: #dededd;
    --dark-gray: #6b7880;
    --paper: #ffffff;
    --backdrop: #1f1f1f;
    --ink: #222222;
  }
  * { box-sizing: border-box; margin: 0; padding: 0; }
  html, body {
    width: 1200px; height: 900px; overflow: hidden;
    background: var(--backdrop);
    font-family: "Ubuntu", sans-serif;
  }
  .canvas { position: relative; width: 1200px; height: 900px; }

  .card {
    position: absolute;
    width: 560px; height: 320px;
    border-radius: 10px;
    overflow: hidden;
    box-shadow: 0 14px 30px rgba(0,0,0,.45);
  }

  /* Front card */
  .card-front { left: 90px; top: 100px; display: flex; background: var(--paper); }
  .front-brand {
    width: 250px; background: var(--brand-blue);
    display: flex; align-items: center; justify-content: center; gap: 10px;
    padding: 0 18px;
  }
  .brand-mark { width: 14px; height: 14px; background: var(--paper); flex: none; }
  .brand-name {
    color: var(--paper); font-weight: 700; font-size: 22px; line-height: 1.15;
    letter-spacing: .5px;
  }
  .front-details { flex: 1; padding: 22px 0 0; }
  .top-rule { height: 2px; background: var(--brand-blue-deep); margin-bottom: 30px; }
  .person { padding: 0 26px; }
  .person-name { color: var(--brand-blue-deep); font-weight: 700; font-size: 24px; }
  .person-title { color: var(--ink); font-size: 14px; margin-top: 4px; }
  .mid-rule { height: 2px; background: var(--brand-blue-deep); margin: 14px 0 18px; }
  .contact-list { list-style: none; padding: 0 26px; }
  .contact-item {
    display: flex; align-items: flex-start; gap: 12px;
    color: var(--ink); font-size: 13px; line-height: 1.35; margin-bottom: 11px;
  }
  .contact-item svg { width: 16px; height: 16px; flex: none; margin-top: 1px; }
  .contact-address { font-weight: 500; }

  /* Back card */
  .card-back {
    left: 550px; top: 480px; background: var(--brand-blue);
    display: flex; flex-direction: column; align-items: center; justify-content: center;
  }
  .back-brand { display: flex; align-items: center; gap: 16px; }
  .back-brand .brand-mark { width: 22px; height: 22px; }
  .back-brand .brand-name { font-size: 40px; letter-spacing: 1px; }
  .back-rule { width: 380px; height: 2px; background: var(--paper); margin: 22px 0 18px; }
  .website { color: var(--paper); font-size: 17px; }
</style>
</head>
<body>
<main class="canvas">

  <section class="card card-front" aria-label="Business card front">
    <div class="front-brand">
      <span class="brand-mark"></span>
      <span class="brand-name">Belford &amp; Company</span>
    </div>
    <div class="front-details">
      <div class="top-rule"></div>
      <div class="person">
        <h1 class="person-name">Daniel Belford</h1>
        <p class="person-title">President</p>
      </div>
      <div class="mid-rule"></div>
      <ul class="contact-list">
        <li class="contact-item contact-address">
          <svg viewBox="0 0 16 16" aria-hidden="true"><path d="M8 1.5 1 8h2v6.5h4v-4h2v4h4V8h2z" fill="#111"/></svg>
          <span>2400 Harbor Ave., Suite #310<br>Riverside, FL 32000</span>
        </li>
        <li class="contact-item">
          <svg viewBox="0 0 16 16" aria-hidden="true"><path d="M4 1.5 6.3 4.3 5 6.2c.9 2 2.6 3.8 4.8 4.8l1.9-1.3 2.8 2.3-1.4 2.3C7.5 14.2 1.8 8.5 1.7 2.9z" fill="none" stroke="#111" stroke-width="1.3" stroke-linejoin="round"/></svg>
          <span>555 0142 317</span>
        </li>
        <li class="contact-item">
          <svg viewBox="0 0 16 16" aria-hidden="true"><rect x="1.5" y="3.5" width="13" height="9" fill="none" stroke="#111" stroke-width="1.3"/><path d="M1.5 3.5 8 9l6.5-5.5" fill="none" stroke="#111" stroke-width="1.3"/></svg>
          <span>info@belfordandcompany.example</span>
        </li>
      </ul>
    </div>
  </section>

  <section class="card card-back" aria-label="Business card back">
    <div class="back-brand">
      <span class="brand-mark"></span>
      <span class="brand-name">Belford &amp; Company</span>
    </div>
    <div class="back-rule"></div>
    <p class="website">website: belfordandcompany.example</p>
  </section>

</main>
</body>
</html>
```